Digital Album Cover - Where The Quiet River Bends (Piano & Cello)

HiI would like a digital album coverTitle: "Where The Quiet River Bends (Piano & Cello)"Artist: "Lorcan Pettigrew & The Oduya Priscilla"

• Original creativity
• Copyrighted images

```html
<!DOCTYPE html>
<html lang="en">
<head>
<meta charset="utf-8">
<title>Where The Quiet River Bends (Piano &amp; Cello) – Album Cover</title>
<link rel="stylesheet" href="https://fonts.googleapis.com/css2?family=Abril+Fatface&family=Great+Vibes&family=Playfair+Display:wght@800&display=swap">
<style>
  :root {
    --page-bg: #f4f4f4;
    --night-black: #05060d;
    --night-navy: #0c1030;
    --night-blue: #2a3ec8;
    --glow-violet: #6a63e0;
    --glow-white: #dfe6ff;
    --ground-dark: #04050b;
    --title-ice: #d9eefc;
    --accent-rose: #c23552;
  }
  * { margin: 0; padding: 0; box-sizing: border-box; }
  html, body {
    width: 1200px;
    height: 1000px;
    overflow: hidden;
    background: var(--page-bg);
  }
  .album-cover {
    position: absolute;
    left: 155px;
    top: 42px;
    width: 896px;
    height: 898px;
    overflow: hidden;
    background: var(--night-black);
  }
  .cover-artwork {
    position: absolute;
    inset: 0;
    background:
      linear-gradient(to bottom, transparent 0%, transparent 70%, var(--ground-dark) 78%, var(--ground-dark) 100%),
      radial-gradient(circle at 617px 254px, var(--glow-white) 0%, #a9b4ff 9%, var(--glow-violet) 17%, #2f3aa8 35%, transparent 62%),
      linear-gradient(to bottom, var(--night-black) 0%, var(--night-navy) 40%, var(--night-blue) 72%, var(--night-black) 100%);
  }
  .cover-title {
    position: absolute;
    left: 57px;
    top: 330px;
    font-family: "Abril Fatface", "Playfair Display", serif;
    color: var(--title-ice);
    font-size: 48px;
    line-height: 58px;
    font-weight: 400;
  }
  .cover-title .title-line { display: block; white-space: nowrap; }
  .cover-title .title-accent {
    font-family: "Great Vibes", cursive;
    color: var(--accent-rose);
    font-size: 64px;
    margin-right: 6px;
  }
  .cover-title .title-edition {
    display: block;
    margin-left: 140px;
    margin-top: -14px;
    font-size: 22px;
    line-height: 26px;
  }
  .cover-artist {
    position: absolute;
    left: 0;
    right: 0;
    top: 800px;
    text-align: center;
    font-family: "Playfair Display", serif;
    font-weight: 800;
    font-size: 25px;
    letter-spacing: 1.5px;
    text-transform: uppercase;
    color: var(--title-ice);
  }
</style>
</head>
<body>
  <div class="album-cover">
    <div class="cover-artwork" role="img" aria-label="Night sky full of stars with a glowing full moon, a couple embracing in silhouette on a dark dune below"></div>
    <h1 class="cover-title">
      <span class="title-line">where the quiet</span>
      <span class="title-line"><span class="title-accent">River</span>bends</span>
      <span class="title-edition">(piano &amp; cello)</span>
    </h1>
    <p class="cover-artist">Lorcan Pettigrew &amp; The Oduya Priscilla</p>
  </div>
</body>
</html>
```